Brochure, website and corporate stationary Design Project

Project scope:
1 x brochure (A4 insert) design
1 x brochure folder design (both external pages and one internal (there will be a few lines of text on the left inside page). The internal right side page will be a pocket for brochures (A4 inserts)
1 x corporate stationary pack (Business Card, logo (a proper logo file format needs to be produced), Letterhead and Envelope)
1 x concept design for our website. You dont need to do the coding. What you need to deliver is the design in a standard format (i.e. photoshop or blend)
Summary: the scope of the project is to design our brochure and its brochure folder, corporate stationary design and graphics concept design for our website. You should also consider our existing logo when performing the above design work (you can modify the logo slightly if you think it would improve look and feel and relevancy to overall design).
• We are a small IT services company
• The folder will be used to hold the brochures (inserts). The folder will be given to prospect customers (see attached a sample service brochure called “VelmaroX User support services Ver0.1.docx”)
• On the cover of the folder, we want to have a design that uses keywords / phrases that reflects our main services (see attached file called “Phrases for presentation folder.docs”). Please note that not all phrases have to be used, use a logic in which ones or add new suggestions
• Inside the folder, at left side we want to have a short text explaining about our services a bit (see attached file called “Brochure Main section v0.91.docx”)
• All designs (corporate stationary, brochure, folder, web, etc.) must be consistent with each other and follow same concept, colour scheme, etc
• you are allowed to do minor changes to our existing logo if you have good reason to do so (see attached logo)
• We want our website design to be simple, elegant, not very colourful, light. HTML5. No flash. (you dont need to do the actual coding of the website, just deliver the design in Photoshop, Blend or any other standard format) With minimal menu items such as: home, services, about us, news, contact us, and other important ones if any. Same colour and design scheme as corporate stationary and brochures
• The company name “VelmaroX” is derived from the Swedish word “Grön” (meaning green) and “roX” which stands for technology but spelled with a “Q” to resemble Quality. The corporate green colour comes from the word “Grön”.
• All templates must be delivered in a standard editable format
Reason: To provide more time to the designers to come with their design submissions.
please note that we more than doubled the budget for this project
Target Market(s)
We deliver IT services to companies of 3-4 employees upto 200-300 employees. The brochures are intended for prospect customers (non IT people)
Industry/Entity Type
Business
Look and feel

```html
<!DOCTYPE html>
<html lang="en">
<head>
<meta charset="utf-8">
<title>VelmaroX – Corporate Stationery</title>
<link href="https://fonts.googleapis.com/css2?family=Open+Sans:wght@400;700&display=swap" rel="stylesheet">
<style>
  :root {
    --brand-green: #3a6650;
    --page-bg: #e6e7e8;
    --paper: #ffffff;
    --ink: #2b2b2b;
    --ink-soft: #555555;
    --ghost: #c6c6c6;
    --on-green: #ffffff;
    --on-green-soft: rgba(255,255,255,0.78);
  }
  * { margin: 0; padding: 0; box-sizing: border-box; }
  html, body { width: 1200px; height: 818px; overflow: hidden; }
  body {
    position: relative;
    background: var(--page-bg);
    font-family: "Open Sans", Arial, sans-serif;
  }
  .wordmark { font-weight: 700; letter-spacing: 0.02em; line-height: 1; white-space: nowrap; }

  /* Letterhead */
  .letterhead {
    position: absolute; left: 18px; top: 18px; width: 607px; height: 784px;
    background: var(--paper); overflow: hidden;
  }
  .letterhead__strip {
    position: absolute; left: 552px; top: 0; width: 55px; height: 660px;
    background: var(--brand-green); border-bottom-left-radius: 26px;
  }
  .letterhead__contact {
    position: absolute; left: 14px; bottom: 34px;
    writing-mode: vertical-rl; transform: rotate(180deg);
    color: var(--on-green-soft); font-size: 7.5px; white-space: nowrap;
  }
  .letterhead__contact b { color: var(--on-green); font-weight: 700; }
  .letterhead__ghost {
    position: absolute; left: 305px; top: 380px;
    transform: translate(-50%, -50%) rotate(-42deg);
    font-size: 106px; color: var(--ghost);
  }
  .letterhead__logo {
    position: absolute; left: 445px; top: 712px; font-size: 27px; color: var(--ink);
  }

  /* Envelope */
  .envelope { position: absolute; left: 0; top: 0; width: 1200px; height: 818px; }
  .envelope__face { fill: var(--paper); }
  .envelope__flap { fill: var(--brand-green); }
  .envelope__logo {
    position: absolute; left: 739px; top: 180px; font-size: 29px; color: var(--ink);
  }
  .envelope__contact {
    position: absolute; left: 739px; top: 281px;
    font-size: 7.8px; line-height: 9px; color: var(--ink-soft);
  }
  .envelope__contact dt { color: var(--ink); font-weight: 700; }
  .envelope__contact dd { margin-bottom: 8px; }

  /* Business cards */
  .card {
    position: absolute; top: 656px; width: 249px; height: 142px;
    background: var(--brand-green); color: var(--on-green);
  }
  .card--front { left: 658px; }
  .card--back { left: 932px; }
  .card__logo {
    position: absolute; right: 20px; top: 22px; font-size: 25px;
  }
  .card__contact {
    position: absolute; right: 20px; top: 56px; text-align: right;
    font-size: 5.6px; line-height: 6.6px; color: var(--on-green-soft);
  }
  .card__contact dt { color: var(--on-green); font-weight: 700; }
  .card__contact dd { margin-bottom: 4px; }
  .card__tagline {
    position: absolute; left: 26px; top: 84px;
    font-size: 8.8px; font-weight: 700; line-height: 10px;
  }
  .card__tagline span { display: block; padding-left: 6px; }
  .card__services {
    position: absolute; right: 19px; top: 9px; list-style: none; text-align: right;
    font-size: 5px; line-height: 5.4px; color: var(--on-green-soft);
  }
</style>
</head>
<body>

  <section class="letterhead" aria-label="Letterhead">
    <div class="wordmark letterhead__ghost" aria-hidden="true">VELMAROX</div>
    <div class="letterhead__strip">
      <p class="letterhead__contact">
        <b>Visit Address</b> Building 7, 3rd Floor, Harbor Tech Park, Lindvale &nbsp;|&nbsp;
        <b>Mail Address</b> PO BOX: 418 306, Harbor Tech Park, Lindvale &nbsp;|&nbsp;
        <b>Phone</b> +44 55 2038164 &nbsp;|&nbsp; <b>Fax</b> +44 5 772 3091
      </p>
    </div>
    <div class="wordmark letterhead__logo">VELMAROX</div>
  </section>

  <section aria-label="Envelope">
    <svg class="envelope" viewBox="0 0 1200 818" aria-hidden="true">
      <path class="envelope__flap" d="M715,154 L715,62 Q715,18 759,18 L1045,18 Q1089,18 1089,62 L1089,154 Z"/>
      <path class="envelope__flap" d="M715,154 L694,154 Q660,157 658,192 L658,386 L715,403 Z"/>
      <path class="envelope__flap" d="M1089,154 L1120,154 Q1153,157 1155,192 L1155,386 L1089,403 Z"/>
      <path class="envelope__flap" d="M715,403 L1089,403 L1089,597 L715,597 Z"/>
      <rect class="envelope__face" x="715" y="154" width="374" height="249"/>
    </svg>
    <div class="wordmark envelope__logo">VELMAROX</div>
    <dl class="envelope__contact">
      <dt>Visit Address</dt>
      <dd>Building 7, 3rd Floor<br>Harbor Tech Park, Lindvale</dd>
      <dt>Mail Address</dt>
      <dd>PO BOX: 418 306<br>Harbor Tech Park, Lindvale</dd>
      <dt>Phone</dt>
      <dd style="margin-bottom:0">+44 55 2038164</dd>
      <dt>Fax</dt>
      <dd>+44 5 772 3091</dd>
    </dl>
  </section>

  <section class="card card--front" aria-label="Business card front">
    <div class="wordmark card__logo">VELMAROX</div>
    <dl class="card__contact">
      <dt>Visit Address</dt>
      <dd>Building 7, 3rd Floor<br>Harbor Tech Park, Lindvale</dd>
      <dt>Mail Address</dt>
      <dd>PO BOX: 418 306<br>Harbor Tech Park, Lindvale</dd>
      <dt>Phone</dt>
      <dd>+44 55 2038164</dd>
      <dt>Fax</dt>
      <dd>+44 5 772 3091</dd>
    </dl>
    <p class="card__tagline">Grow your<span>business with us!</span></p>
  </section>

  <section class="card card--back" aria-label="Business card back">
    <ul class="card__services">
      <li>IT support</li>
      <li>IT Service management</li>
      <li>IT Helpdesk services</li>
      <li>IT security</li>
      <li>IT infrastructure</li>
      <li>Network</li>
      <li>Cloud services</li>
      <li>Hosted email</li>
      <li>Hosted groupware</li>
      <li>Application hosting</li>
      <li>Cloud email</li>
      <li>Mail clients</li>
      <li>Office suites</li>
      <li>Web development</li>
      <li>Business Process Management</li>
      <li>IT Management consultancy</li>
      <li>Business applications</li>
      <li>ERP</li>
      <li>CRM</li>
      <li>Accounting software</li>
      <li>SEO</li>
      <li>Search engine optimization</li>
    </ul>
  </section>

</body>
</html>
```